Dear Designer
I am looking for some proposal for the graphic design of our new web site
www.drelvox.com; you can find in real time the developper version on : drelvox.tabrino.info/?id=308

We do not need web page programing... no IT stuff .. only to provide me graphic contents for some pages:
- home
- contact us
- product page
- download page
- blog page
- application page
Pls advise me back asap
Thank you
Henrik

```html
<!DOCTYPE html>
<html lang="en">
<head>
<meta charset="utf-8">
<title>Drelvox Power Transmission</title>
<link href="https://fonts.googleapis.com/css2?family=Montserrat:wght@600;700;800&family=Open+Sans:wght@400;600;700&display=swap" rel="stylesheet">
<style>
:root{
  --blue:#1b6ec2;
  --blue-dark:#1457a3;
  --ink:#222831;
  --text:#555b63;
  --pale:#e7eef7;
  --field-line:#c9ccd1;
  --white:#ffffff;
}
*{box-sizing:border-box;margin:0;padding:0}
html,body{width:1200px;height:3013px;overflow:hidden}
body{position:relative;font-family:"Open Sans",Arial,sans-serif;color:var(--text);background:var(--white)}
.abs{position:absolute}

/* header */
.top-rule{left:0;top:0;width:1200px;height:3px;background:var(--blue)}
.brand{left:144px;top:26px;font-family:"Montserrat",Arial,sans-serif;font-weight:800;font-size:44px;letter-spacing:1px;color:var(--blue);line-height:60px}
.contact-chip{top:3px;height:55px;background:var(--blue);color:var(--white);font-family:"Montserrat",Arial,sans-serif;font-weight:700;font-size:14px;display:flex;align-items:center;justify-content:center;gap:12px}
.chip-phone{left:647px;width:180px}
.chip-mail{left:830px;width:224px}
.main-nav{left:0;top:74px;width:1200px;font-family:"Montserrat",Arial,sans-serif;font-weight:700;font-size:13px;color:var(--ink)}
.main-nav span{position:absolute;top:2px;white-space:nowrap}
.main-nav .is-active{color:var(--blue)}
.nav-dot{left:445px;top:61px;width:9px;height:9px;border-radius:50%;background:#bfc3c8}

/* hero */
.hero{left:0;top:108px;width:1200px;height:560px;background:linear-gradient(110deg,#2f8a78 0%,#2a6f8d 25%,#1d4f87 50%,#1e6a9b 75%,#174a7e 100%)}
.hero-glow{left:0;top:108px;width:1200px;height:560px;background:radial-gradient(ellipse 380px 300px at 0% 100%,rgba(228,176,60,.75),transparent 70%),radial-gradient(circle 330px at 830px 330px,rgba(120,210,230,.35),transparent 70%)}
.hero-title{left:143px;top:282px;font-family:"Montserrat",Arial,sans-serif;font-weight:800;font-size:67px;line-height:64px;color:var(--white);text-shadow:3px 3px 6px rgba(0,0,0,.45)}
.btn{display:flex;align-items:center;justify-content:center;border-radius:24px;font-family:"Open Sans",Arial,sans-serif;font-weight:700;font-size:15px;letter-spacing:.3px}
.btn-hero{left:144px;top:430px;width:154px;height:45px;background:var(--blue);color:var(--white)}

/* welcome */
.welcome{left:0;top:668px;width:1200px;height:465px;background:var(--blue);color:var(--white);text-align:center}
.emblem{left:541px;top:608px;width:118px;height:118px;border-radius:50%;background:var(--white);display:flex;align-items:center;justify-content:center}
.emblem i{display:block;width:70px;height:70px;border-radius:50%;border:14px solid var(--blue)}
.welcome-kicker{position:absolute;left:0;top:109px;width:1200px;font-family:"Montserrat",Arial,sans-serif;font-weight:700;font-size:16px}
.welcome-title{position:absolute;left:0;top:133px;width:1200px;font-family:"Montserrat",Arial,sans-serif;font-weight:700;font-size:34px}
.welcome p{position:absolute;left:240px;width:720px;font-size:13.4px;line-height:21px}
.welcome .p1{top:186px}
.welcome .p2{top:269px}
.btn-learn{left:523px;top:998px;width:154px;height:46px;background:var(--white);color:var(--blue)}

/* features */
.features-bg{left:0;top:1132px}
.frame{width:471px;height:324px;background:var(--blue);border-radius:162px 0 0 162px}
.frame.flip{border-radius:0 162px 162px 0}
.frame .photo{position:absolute;left:19px;top:12px;right:18px;bottom:12px;border-radius:150px 0 0 150px}
.frame.flip .photo{left:18px;right:19px;border-radius:0 150px 150px 0}
.photo-1{background:linear-gradient(120deg,#c9c2b8,#8a7a66 55%,#b7a892)}
.photo-2{background:linear-gradient(120deg,#a0603f,#7a4d35 45%,#d8d2c8 75%,#6b4a33)}
.photo-3{background:linear-gradient(120deg,#e9edf0,#d4dbe0 50%,#e4c27a 90%)}
.badge{position:absolute;width:84px;height:84px;border-radius:50%;background:var(--white);display:flex;align-items:center;justify-content:center}
.feature-title{font-family:"Montserrat",Arial,sans-serif;font-weight:700;font-size:28px;color:var(--ink)}
.feature-text{font-size:13.4px;line-height:21px;width:434px}

/* contact */
.contact{left:0;top:2398px;width:1200px;height:526px;background:linear-gradient(180deg,#eef1f4,#f6f7f9 60%,#eef0f2)}
.contact-title{left:0;top:2490px;width:1200px;text-align:center;font-family:"Montserrat",Arial,sans-serif;font-weight:700;font-size:33px;color:var(--ink)}
.info-card{left:144px;top:2552px;width:435px;height:275px;background:linear-gradient(135deg,var(--blue),var(--blue-dark));color:var(--white);padding:38px 0 0 64px}
.info-card h3{font-family:"Open Sans",Arial,sans-serif;font-weight:700;font-size:20px;margin-bottom:28px}
.info-row{display:flex;gap:14px;font-size:20px;line-height:32px}
.info-row svg{flex:0 0 20px;margin-top:7px}
.field{left:623px;height:45px;border:1px solid var(--field-line);background:var(--white);font-size:13px;color:#6b7078;padding:14px 18px}
.btn-submit{left:623px;top:2784px;width:211px;height:44px;background:var(--blue);color:var(--white);font-family:"Open Sans",Arial,sans-serif;font-weight:700;font-size:13px;display:flex;align-items:center;justify-content:center}

/* footer */
.footer{left:0;top:2924px;width:1200px;height:89px;background:var(--blue);color:var(--white);font-size:13.5px;font-weight:600;text-align:center;line-height:89px}
</style>
</head>
<body>

<header>
  <div class="abs top-rule"></div>
  <div class="abs brand">DRELVOX</div>
  <div class="abs contact-chip chip-phone">
    <svg width="13" height="13" viewBox="0 0 24 24" fill="#fff"><path d="M6.6 10.8a15.1 15.1 0 0 0 6.6 6.6l2.2-2.2a1 1 0 0 1 1-.25 11.4 11.4 0 0 0 3.6.57 1 1 0 0 1 1 1V20a1 1 0 0 1-1 1A17 17 0 0 1 3 4a1 1 0 0 1 1-1h3.5a1 1 0 0 1 1 1c0 1.25.2 2.45.57 3.57a1 1 0 0 1-.25 1z"/></svg>
    + (1) 555 204 7788
  </div>
  <div class="abs contact-chip chip-mail">
    <svg width="14" height="11" viewBox="0 0 24 18" fill="#fff"><path d="M0 2l12 8 12-8V0H0zM0 4.5V18h24V4.5l-12 8z"/></svg>
    info@drelvoxpower.com
  </div>
  <div class="abs nav-dot"></div>
  <nav class="abs main-nav">
    <span class="is-active" style="left:430px">HOME</span>
    <span style="left:500px">PRODUCT</span>
    <span style="left:594px">APPLICATIONS</span>
    <span style="left:720px">COMPANY</span>
    <span style="left:816px">DOWNLOADS</span>
    <span style="left:931px">BLOG</span>
    <span style="left:996px">CONTACT</span>
  </nav>
</header>

<section>
  <div class="abs hero" role="img" aria-label="Power transmission pylon beside a glowing digital globe"></div>
  <div class="abs hero-glow"></div>
  <h1 class="abs hero-title">DRELVOX POWER<br>TRANSMISSION</h1>
  <div class="abs btn btn-hero">GET STARTED</div>
</section>

<section class="abs welcome">
  <div class="welcome-kicker">WELCOME TO</div>
  <h2 class="welcome-title">DRELVOX POWER TRANSMISSION</h2>
  <p class="p1">Drelvox Power Transmission designs, engineers, produces, and distributes high-quality power transmission technologies and components for world-class industrial applications, with the goal of increasing the efficiency of its customers' machines and systems.</p>
  <p class="p2">We represent a wide variety of clients and are continually providing innovative ideas to life. Our reputation is built on the undeniable quality of every product we make.</p>
</section>
<div class="abs emblem"><i></i></div>
<div class="abs btn btn-learn">LEARN MORE</div>

<section>
  <svg class="abs features-bg" width="1200" height="1266" viewBox="0 0 1200 1266">
    <polygon points="468,134 968,634 468,1134 -32,634" fill="#e7eef7"/>
  </svg>

  <div class="abs frame" style="left:125px;top:1216px">
    <div class="photo photo-1" role="img" aria-label="Child working on a laptop with an adult beside him"></div>
    <div class="badge" style="left:356px;top:22px">
      <svg width="44" height="44" viewBox="0 0 44 44" fill="none" stroke="#1b6ec2" stroke-width="2"><circle cx="22" cy="20" r="6"/><circle cx="22" cy="20" r="11" stroke-dasharray="4 3"/><path d="M6 40h10l8-4M38 4H28l-8 4"/></svg>
    </div>
  </div>
  <h3 class="abs feature-title" style="left:620px;top:1314px">RELIABLE ALTERNATIVE</h3>
  <p class="abs feature-text" style="left:621px;top:1362px">What you expect is what you get: a Drelvox solution you can rely on as a formidable switch alternative that works thanks to rigorous design and development processes as well as regular quality control management.</p>

  <div class="abs frame flip" style="left:602px;top:1605px">
    <div class="photo photo-2" role="img" aria-label="Team reviewing documents and tablets around a wooden table"></div>
    <div class="badge" style="left:28px;top:22px">
      <svg width="44" height="44" viewBox="0 0 44 44" fill="none" stroke="#1b6ec2" stroke-width="2"><rect x="14" y="6" width="20" height="16"/><path d="M22 6v7l2-2 2 2V6M4 34l10-6h12l-4 4h-8M22 32l14-6-10 12H12"/></svg>
    </div>
  </div>
  <h3 class="abs feature-title" style="left:141px;top:1702px">SMART PRODUCTS</h3>
  <p class="abs feature-text" style="left:144px;top:1750px">To respond to a wide variety of industries or applications, we design and manufacture a large and feature-rich range of power transmission and conveying belt in class products that have been strongly engineered towards meeting the needed standards without unnecessary added costs</p>

  <div class="abs frame" style="left:125px;top:1992px">
    <div class="photo photo-3" role="img" aria-label="Smiling businesswoman working at a desk"></div>
    <div class="badge" style="left:356px;top:22px">
      <svg width="44" height="44" viewBox="0 0 44 44" fill="none" stroke="#1b6ec2" stroke-width="2"><circle cx="22" cy="18" r="13"/><circle cx="22" cy="18" r="9"/><path d="M17 18l4 4 6-7M14 29l-5 11 6-2 3 5 4-10M30 29l5 11-6-2-3 5-4-10"/></svg>
    </div>
  </div>
  <h3 class="abs feature-title" style="left:620px;top:2090px">TRUSTABLE EXPERIENCE</h3>
  <p class="abs feature-text" style="left:621px;top:2138px">You can trust our decades of valuable experiences on a global scale to back up your decision. Already well represented in many key countries, we are one of the top global players</p>
</section>

<section>
  <div class="abs contact" role="img" aria-label="Faint power line pylons in a pale sky"></div>
  <h2 class="abs contact-title">CONTACT US</h2>
  <div class="abs info-card">
    <h3>DRELVOX POWER TRANSMISSION</h3>
    <div class="info-row">
      <svg width="14" height="18" viewBox="0 0 14 20" fill="#fff"><path d="M7 0a7 7 0 0 0-7 7c0 5 7 13 7 13s7-8 7-13a7 7 0 0 0-7-7zm0 9.5A2.5 2.5 0 1 1 7 4.5a2.5 2.5 0 0 1 0 5z"/></svg>
      <span>48 Harlow Crescent<br>Marlow Ridge, ON K2B 7T4</span>
    </div>
    <div class="info-row">
      <svg width="20" height="15" viewBox="0 0 24 18" fill="#fff"><path d="M0 2l12 8 12-8V0H0zM0 4.5V18h24V4.5l-12 8z"/></svg>
      <span>info@drelvoxpower.com</span>
    </div>
    <div class="info-row">
      <svg width="17" height="17" viewBox="0 0 24 24" fill="#fff"><path d="M6.6 10.8a15.1 15.1 0 0 0 6.6 6.6l2.2-2.2a1 1 0 0 1 1-.25 11.4 11.4 0 0 0 3.6.57 1 1 0 0 1 1 1V20a1 1 0 0 1-1 1A17 17 0 0 1 3 4a1 1 0 0 1 1-1h3.5a1 1 0 0 1 1 1c0 1.25.2 2.45.57 3.57a1 1 0 0 1-.25 1z"/></svg>
      <span>+ (1) 555 204 7788</span>
    </div>
  </div>
  <div class="abs field" style="top:2551px;width:211px">Name</div>
  <div class="abs field" style="left:844px;top:2551px;width:211px">Phone</div>
  <div class="abs field" style="top:2608px;width:432px">Email address</div>
  <div class="abs field" style="top:2664px;width:432px;height:109px">Message</div>
  <div class="abs btn-submit">SUBMIT</div>
</section>

<footer class="abs footer">© 2021 Company name | All Rights Reserved | Terms and Conditions</footer>

</body>
</html>
```